Letterhead & Powerpoint Template Design for a Commercial Solar Company

We need these designs for a growing commercial solar company in Austin Texas. We specialize in large-scale/commercial installations. Any assets we design should have the following elements/considerations.
-Authoritative
-Crisp
-Professional
-No Cartoonish Graphics / nothing "cute"
-Should feel more like an engineering firm style than what you typically solar companies
-Not overwhelming

Ultimately are looking for the following in this design
-Letterhead design
-Powerpoint Design (horizontal Pitch deck with a title page design template 3-4 different layouts that we can alternate or use as needed)
-Proposal Design (Vertical layout that has a very professional title page and then just a standard template for interior pages)
-Business Card

Preferred fonts are Inter & Roboto

Dropbox of photo assets to use - https://www.filevaultor.net/sh/pwmtrebxnhqz4ka/KKRfe527ytbwQmZdHrVnPo8Zc?dl=0

Target Market(s)

C-Suites, Decision Makers, Commercial property owners

Industry/Entity Type

Solar

Font styles to use
Other font styles liked:
• Inter (Primary) Roboto (Secondary)

Colors

Designer to choose colors to be used in the design.

Requirements
Must have
• Authoritative Crisp Styling
Should not have
• cartoonish or bubbly graphics.

```html
<!DOCTYPE html>
<html lang="en">
<head>
<meta charset="utf-8">
<title>Vantor Solar — Brand Stationery, Proposal and Presentation</title>
<link rel="stylesheet" href="https://fonts.googleapis.com/css2?family=Roboto:wght@300;400;500;700;900&family=Roboto+Condensed:wght@700&family=Inter:wght@400;500;600&display=swap">
<style>
:root{
  --orange:#f15a29;
  --orange-soft:#f7a07f;
  --ink:#333333;
  --text:#6f6f6f;
  --line:#c9c9c9;
  --paper:#ffffff;
  --panel:#eeeeee;
  --board-top:#dcdddf;
  --board-mid:#c7c9cc;
  --board-low:#e3e4e6;
  --sky:#d3dadf;
  --roof:#9a9c9b;
  --vest:#d3d85a;
  --helmet:#4a4d51;
  --shadow:#6d6f70;
}
*{box-sizing:border-box;margin:0;padding:0}
html,body{width:1200px;height:3028px;overflow:hidden}
body{position:relative;font-family:"Roboto",sans-serif;color:var(--ink);background:var(--board-low)}
.abs{position:absolute}
.band{position:absolute;left:0;width:1200px}
.band-stationery{top:0;height:1030px;background:var(--board-top)}
.band-proposal{top:1030px;height:813px;background:var(--board-mid)}
.band-deck{top:1843px;height:1185px;background:var(--board-low)}
.section-label{position:absolute;font-family:"Inter",sans-serif;font-size:18px;color:#555;font-weight:400}
.section-label.light{color:#fff}

.brand{position:absolute;font-family:"Roboto",sans-serif;font-weight:400;color:var(--ink);line-height:1;text-align:center}
.brand .b1{display:block;letter-spacing:.08em}
.brand .b2{display:block;letter-spacing:.42em;padding-left:.42em}
.brand.white{color:#fff}

.page{position:absolute;background:var(--paper);overflow:hidden}

/* photo areas: soft tonal gradients in the scene's main colours */
.photo{position:absolute;
  background:
    radial-gradient(ellipse 28% 38% at 64% 58%, rgba(211,216,90,.9), rgba(211,216,90,0) 70%),
    radial-gradient(ellipse 16% 14% at 60% 26%, rgba(74,77,81,.85), rgba(74,77,81,0) 72%),
    radial-gradient(ellipse 40% 30% at 30% 85%, rgba(110,112,113,.7), rgba(110,112,113,0) 70%),
    linear-gradient(180deg,var(--sky) 0%,#c4cbd0 38%,var(--roof) 70%,#7f8182 100%);}
.photo.panel-carry{
  background:
    radial-gradient(ellipse 22% 40% at 78% 62%, rgba(211,216,90,.92), rgba(211,216,90,0) 70%),
    radial-gradient(ellipse 30% 55% at 38% 55%, rgba(95,110,128,.75), rgba(95,110,128,0) 72%),
    radial-gradient(ellipse 14% 12% at 76% 22%, rgba(235,235,235,.9), rgba(235,235,235,0) 72%),
    linear-gradient(160deg,#f4f5f6 0%,#dfe3e6 40%,#b7bcc0 100%);}
.photo.plans{
  background:
    radial-gradient(ellipse 40% 30% at 50% 40%, rgba(250,250,250,.9), rgba(250,250,250,0) 70%),
    linear-gradient(135deg,#8f98a0,#c9d0d5 55%,#e6e9eb);}

/* business card */
.card-name{font-size:15px;font-weight:700;color:var(--ink);letter-spacing:.02em}
.card-name span{color:var(--orange)}
.card-role{font-size:11px;color:var(--text);margin-top:2px}
.contact-row{display:flex;align-items:center;gap:6px;font-size:10px;color:var(--text);margin-top:7px}
.icon-sq{width:11px;height:11px;background:var(--orange);border-radius:2px;display:inline-block;flex:none;position:relative}
.foot-band{position:absolute;left:0;height:14px;background:var(--orange);color:#fff;font-size:9.5px;line-height:14px;padding-left:36px;clip-path:polygon(0 0,100% 0,calc(100% - 12px) 100%,0 100%)}
.foot-rule{position:absolute;height:2px;background:#888}

/* letterhead */
.lh-contacts{position:absolute;right:26px;top:36px;text-align:right;font-size:11px;color:var(--text)}
.lh-contacts div{display:flex;justify-content:flex-end;align-items:center;gap:6px;margin-bottom:8px}
.lh-name{position:absolute;left:36px;top:196px;font-size:21px;color:var(--orange);letter-spacing:.02em}
.lh-details{position:absolute;left:36px;top:233px;font-size:11.5px;color:var(--text);line-height:1.35}
.lh-details p{margin-bottom:7px}
.lh-date{position:absolute;right:28px;top:278px;font-size:13px;color:var(--ink)}
.lh-body{position:absolute;left:36px;right:28px;top:320px;font-size:11.8px;line-height:1.38;color:#8a8a8a;text-align:justify}
.lh-body p{margin-bottom:18px}
.lh-sign-role{position:absolute;right:40px;top:672px;font-size:14px;color:var(--text)}

/* proposal */
.head-block{position:absolute;text-align:right;font-family:"Roboto",sans-serif;line-height:1.05}
.head-block .h1{color:var(--orange);font-weight:700}
.head-block .h2{color:var(--ink);font-weight:700;letter-spacing:.02em}
.head-block .h3{color:var(--ink);font-weight:700;margin-top:6px}
.cover-title{position:absolute;left:36px;color:#fff;line-height:1}
.cover-list{position:absolute;right:24px;text-align:right;font-size:12px;color:var(--ink);line-height:1.75}
.cover-url{position:absolute;left:32px;top:636px;font-size:12px;letter-spacing:.22em;color:var(--ink)}
.cover-url span{color:var(--orange)}

/* slides */
.slide{position:absolute;width:362px;height:203px;background:var(--paper);overflow:hidden}
.slide .foot{position:absolute;left:12px;bottom:4px;font-size:9px;color:#777;line-height:1}
.slide .foot small{display:block;font-size:4px;letter-spacing:.4em;color:#999;margin-top:1px}
.slide .rule{position:absolute;left:40px;right:6px;bottom:10px;height:1px;background:var(--orange)}
.slide .num{position:absolute;right:8px;bottom:6px;font-size:5px;color:#777}
.s-title{position:absolute;font-weight:700;line-height:1;color:var(--ink)}
.s-title .o{color:var(--orange)}
.tiny{font-size:4.4px;line-height:1.4;color:#777}
.mini-head{font-size:7px;color:var(--orange);font-weight:500}
.dot-orange{display:inline-block;width:4px;height:4px;border-radius:50%;background:var(--orange);margin-right:3px}
.soc{display:inline-block;width:9px;height:9px;background:var(--orange);border-radius:2px;margin-left:3px}
</style>
</head>
<body>

<!-- ===== Stationery ===== -->
<div class="band band-stationery"></div>
<div class="section-label" style="left:62px;top:210px">Business Card</div>
<div class="section-label" style="left:532px;top:48px">Letterhead</div>

<section class="page business-card-front" style="left:62px;top:240px;width:423px;height:252px">
  <div class="brand" style="left:38px;top:84px;font-size:44px"><span class="b1">VANTOR</span><span class="b2" style="font-size:20px;margin-top:4px">SOLAR</span></div>
  <div class="abs" style="left:220px;top:28px;width:1px;height:170px;background:linear-gradient(#fff,#e2e2e2,#fff)"></div>
  <div class="abs" style="left:238px;top:64px">
    <div class="card-name">DANA <span>WHITFIELD</span></div>
    <div class="card-role">Managing Director</div>
    <div class="abs" style="top:36px;left:0;width:150px;height:1px;background:var(--orange)"></div>
    <div style="margin-top:14px">
      <div class="contact-row"><span class="icon-sq"></span>+00 555 010 20</div>
      <div class="contact-row"><span class="icon-sq"></span>hello@vantormail.com</div>
      <div class="contact-row"><span class="icon-sq"></span>www.vantorsolar.example</div>
    </div>
  </div>
  <div class="foot-band" style="top:210px;width:280px">1180 Ridgeline Blvd, Austin, TX 78701</div>
  <div class="foot-rule" style="top:215px;left:272px;right:0"></div>
</section>

<section class="page business-card-back" style="left:60px;top:544px;width:423px;height:255px;background:var(--orange)">
  <div class="brand white" style="left:125px;top:92px;font-size:48px"><span class="b1">VANTOR</span><span class="b2" style="font-size:21px;margin-top:5px">SOLAR</span></div>
</section>

<section class="page letterhead" style="left:528px;top:82px;width:618px;height:872px">
  <div class="brand" style="left:36px;top:36px;font-size:38px"><span class="b1">VANTOR</span><span class="b2" style="font-size:17px;margin-top:5px;color:var(--ink)">SOLAR</span></div>
  <div class="lh-contacts">
    <div>+00 555 010 20 <span class="icon-sq"></span></div>
    <div>hello@vantormail.com <span class="icon-sq"></span></div>
    <div>www.vantorsolar.example <span class="icon-sq"></span></div>
  </div>
  <div class="lh-name">MARA ELLISON</div>
  <div class="lh-details">
    <p>0155-010-246</p>
    <p>info@northfieldpartners.example</p>
    <p style="margin:0">88 Harbor Lane Suite 4</p>
    <p>Dallas, TX 0000</p>
  </div>
  <div class="lh-date">12 December, 2023</div>
  <div class="lh-body">
    <p>Lorem ipsum dolor sit amet, consectetuer adipiscing elit, sed diam nonummy nibh euismod tincidunt ut laoreet dolore magna aliquam erat volutpat. Ut wisi enim ad minim veniam, quis nostrud exerci tation ullamcorper suscipit lobortis nisl ut aliquip ex ea commodo consequat. Duis autem vel eum iriure dolor in hendrerit in vulputate velit esse molestie consequat, vel illum dolore eu feugiat nulla facilisis at vero eros et accumsan et iusto odio dignissim qui blandit praesent luptatum zzril delenit augue duis dolore te feugait nulla facilisi.</p>
    <p>Lorem ipsum dolor sit amet, cons ectetuer adipiscing elit, sed diam nonummy nibh euismod tincidunt ut laoreet dolore magna aliquam erat volutpat. Ut wisi enim ad minim veniam, quis nostrud exerci tation ullamcorper suscipit lobortis nisl ut aliquip ex ea commodo consequat. Lorem ipsum dolor sit amet, consectetuer adipiscing elit, sed diam nonummy nibh euismod tincidunt ut laoreet dolore magna aliquam erat</p>
    <p style="margin-top:34px">Lorem ipsum dolor sit amet, cons ectetuer adipiscing elit, sed diam nonummy nibh euismod tincidunt ut laoreet dolore magna aliquam erat volutpat. Ut wisi enim ad minim veniam, quis nostrud exerci tation ullamcorper suscipit lobortis nisl ut aliquip ex ea commodo consequat. Lorem ipsum dolor sit zamet, consectetuer adipiscing elit, sed diam nonummy nibh euismod tincidunt.</p>
  </div>
  <div class="lh-sign-role">Managing Director</div>
  <div class="abs" role="img" aria-label="Handwritten signature" style="left:466px;top:702px;width:110px;height:48px;background:linear-gradient(90deg,rgba(235,235,235,0),#ececec 30%,#ececec 70%,rgba(235,235,235,0))"></div>
  <div class="foot-band" style="top:832px;width:320px">1180 Ridgeline Blvd, Austin, TX 78701</div>
  <div class="foot-rule" style="top:838px;left:312px;right:0"></div>
</section>

<!-- ===== Proposal ===== -->
<div class="band band-proposal"></div>
<div class="section-label light" style="left:50px;top:1074px">Proposal Design</div>

<section class="page proposal-cover" style="left:50px;top:1118px;width:531px;height:685px">
  <div class="brand" style="left:30px;top:38px;font-size:50px"><span class="b1">VANTOR</span><span class="b2" style="font-size:22px;margin-top:6px">SOLAR</span></div>
  <div class="head-block" style="right:36px;top:24px">
    <div class="h1" style="font-size:24px">Headeline</div>
    <div class="h2" style="font-size:27px">Lorem Ipsum</div>
    <div class="h3" style="font-size:12px">Space Here</div>
  </div>
  <div class="abs" style="left:420px;top:118px;width:111px;height:152px;background:#c5c6c8;border-radius:14px 0 0 14px"></div>
  <svg class="abs" style="left:0;top:110px" width="531" height="520" viewBox="0 0 531 520">
    <defs>
      <linearGradient id="coverBase" x1="0" y1="0" x2="0" y2="1">
        <stop offset="0" stop-color="#cfd5d9"/><stop offset=".45" stop-color="#b3b7b8"/><stop offset="1" stop-color="#6f7172"/>
      </linearGradient>
      <radialGradient id="coverVest" cx=".5" cy=".5" r=".5"><stop offset="0" stop-color="#d6db5e"/><stop offset=".6" stop-color="#c9cf58" stop-opacity=".7"/><stop offset="1" stop-color="#c9cf58" stop-opacity="0"/></radialGradient>
      <radialGradient id="coverHelmet" cx=".5" cy=".5" r=".5"><stop offset="0" stop-color="#3f4246"/><stop offset="1" stop-color="#3f4246" stop-opacity="0"/></radialGradient>
      <radialGradient id="coverSleeve" cx=".5" cy=".5" r=".5"><stop offset="0" stop-color="#f1f1ef"/><stop offset="1" stop-color="#f1f1ef" stop-opacity="0"/></radialGradient>
      <radialGradient id="coverShade" cx=".5" cy=".5" r=".5"><stop offset="0" stop-color="#4e5052"/><stop offset="1" stop-color="#4e5052" stop-opacity="0"/></radialGradient>
      <clipPath id="coverClip"><path d="M152 52 Q160 30 186 30 L492 30 Q514 30 506 52 L404 370 Q396 390 372 390 L70 390 L122 150 Z"/></clipPath>
    </defs>
    <g role="img" aria-label="Photo of a solar installer in a hard hat and safety vest working on a rooftop array" clip-path="url(#coverClip)">
      <rect x="0" y="0" width="531" height="420" fill="url(#coverBase)"/>
      <ellipse cx="250" cy="150" rx="110" ry="80" fill="url(#coverShade)" opacity=".5"/>
      <ellipse cx="330" cy="90" rx="85" ry="62" fill="url(#coverHelmet)"/>
      <ellipse cx="410" cy="170" rx="95" ry="120" fill="url(#coverVest)"/>
      <ellipse cx="300" cy="230" rx="70" ry="60" fill="url(#coverSleeve)" opacity=".8"/>
      <ellipse cx="200" cy="330" rx="150" ry="60" fill="url(#coverShade)" opacity=".6"/>
    </g>
    <path d="M0 197 L362 197 L302 470 Q296 490 274 490 L0 490 Z" fill="var(--orange)" opacity=".93"/>
    <path d="M122 197 L158 104 Q166 86 188 86 L506 86" fill="none" stroke="var(--orange)" stroke-width="2"/>
    <path d="M302 505 L412 505 Q432 505 440 485 L506 270" fill="none" stroke="var(--orange)" stroke-width="2"/>
    <rect x="222" y="-8" width="16" height="64" rx="7" transform="rotate(15 230 24)" fill="var(--ink)"/>
  </svg>
  <div class="cover-title" style="top:352px;font-size:48px;font-weight:400;letter-spacing:.02em">ANNUAL</div>
  <div class="cover-title" style="top:402px;font-size:64px;font-weight:900">REPORT</div>
  <div class="abs" style="left:38px;top:474px;width:68px;height:5px;background:#fff"></div>
  <div class="cover-title" style="top:492px;font-size:82px;font-weight:500">2023</div>
  <div class="abs" style="right:24px;top:550px;font-size:22px;font-weight:500;color:var(--orange)">LOREM IPSUM</div>
  <div class="cover-list" style="top:580px">Lorem ipsum dolor •<br>sit amet, consectetuer •<br>adipiscing elit, sed diam •</div>
  <div class="cover-url">www.<span>vantorsolar</span>.example</div>
</section>

<section class="page proposal-interior" style="left:619px;top:1118px;width:531px;height:685px">
  <div class="brand" style="left:24px;top:24px;font-size:34px"><span class="b1">VANTOR</span><span class="b2" style="font-size:14px;margin-top:4px">SOLAR</span></div>
  <div class="head-block" style="right:36px;top:24px">
    <div class="h1" style="font-size:20px">Headeline</div>
    <div class="h2" style="font-size:21px">Lorem Ipsum</div>
    <div class="h3" style="font-size:10px">Space Here</div>
  </div>
  <div class="abs" style="left:0;right:30px;top:652px;height:3px;background:linear-gradient(90deg,rgba(241,90,41,0),var(--orange) 40%)"></div>
  <div class="abs" style="right:8px;top:647px;font-size:10px;font-weight:700;color:var(--ink);background:#fff;padding:0 3px">02</div>
</section>

<!-- ===== Presentation deck ===== -->
<div class="band band-deck"></div>
<div class="section-label" style="left:50px;top:1878px">Powerpoint Design</div>

<section class="slide slide-title" style="left:50px;top:1918px">
  <div class="photo panel-carry" role="img" aria-label="Photo of two installers carrying a solar panel" style="left:150px;top:22px;width:212px;height:181px;clip-path:polygon(12% 0,100% 0,100% 100%,0 100%)"></div>
  <div class="brand" style="left:12px;top:14px;font-size:26px"><span class="b1">VANTOR</span><span class="b2" style="font-size:11px;margin-top:3px">SOLAR</span></div>
  <div class="abs" style="right:8px;top:8px"><span class="soc"></span><span class="soc"></span><span class="soc"></span><span class="soc"></span></div>
  <div class="abs" style="left:12px;top:110px;font-size:9px;color:var(--ink)">PRESENTATION</div>
  <div class="s-title" style="left:11px;top:122px;font-size:28px;font-family:'Roboto Condensed',sans-serif">BUSINESS</div>
  <div class="s-title" style="left:11px;top:150px;font-size:22px;font-family:'Roboto Condensed',sans-serif"><span class="o">MARKETING</span></div>
  <div class="abs" style="left:12px;top:176px;font-size:7px;letter-spacing:.15em;color:var(--ink)">www.<span style="color:var(--orange)">vantorsolar</span>.example</div>
</section>

<section class="slide slide-contents" style="left:423px;top:1918px">
  <div class="s-title" style="left:26px;top:14px;font-size:18px;font-family:'Roboto Condensed',sans-serif">CONTENTS</div>
  <div class="abs" style="left:26px;top:34px;width:40px;height:2px;background:var(--orange)"></div>
  <div class="abs" style="left:40px;top:50px;width:140px">
    <div class="mini-head"><b style="color:var(--ink)">1.</b> Lorem ipsum</div><div class="tiny" style="padding-left:14px">Lorem ipsum dolor sit amet, consectetuer adipiscing elit, sed diam nonummy nibh</div>
    <div class="mini-head" style="margin-top:22px"><b style="color:var(--ink)">3.</b> Lorem ipsum</div><div class="tiny" style="padding-left:14px">Lorem ipsum dolor sit amet, consectetuer adipiscing elit, sed diam nonummy nibh</div>
    <div class="mini-head" style="margin-top:22px"><b style="color:var(--ink)">5.</b> Lorem ipsum</div><div class="tiny" style="padding-left:14px">Lorem ipsum dolor sit amet, consectetuer adipiscing elit, sed diam nonummy nibh</div>
  </div>
  <div class="abs" style="left:190px;top:50px;width:140px">
    <div class="mini-head"><b style="color:var(--ink)">2.</b> Lorem ipsum</div><div class="tiny" style="padding-left:14px">Lorem ipsum dolor sit amet, consectetuer adipiscing elit, sed diam nonummy nibh</div>
    <div class="mini-head" style="margin-top:22px"><b style="color:var(--ink)">4.</b> Lorem ipsum</div><div class="tiny" style="padding-left:14px">Lorem ipsum dolor sit amet, consectetuer adipiscing elit, sed diam nonummy nibh</div>
    <div class="mini-head" style="margin-top:22px"><b style="color:var(--ink)">6.</b> Lorem ipsum</div><div class="tiny" style="padding-left:14px">Lorem ipsum dolor sit amet, consectetuer adipiscing elit, sed diam nonummy nibh</div>
  </div>
  <div class="foot">VANTOR<small>SOLAR</small></div><div class="rule"></div><div class="num">02</div>
</section>

<section class="slide slide-about" style="left:797px;top:1918px">
  <div class="abs" style="left:18px;top:16px;font-size:10px;color:var(--ink)">ABOUT US</div>
  <div class="s-title" style="left:18px;top:27px;font-size:18px"><span class="o">COMPANY</span></div>
  <div class="abs tiny" style="left:18px;top:50px;width:150px">Lorem ipsum dolor sit amet, consectetuer adipiscing elit, sed diam nonummy nibh euismod tincidunt ut laoreet dolore magna aliquam erat volutpat. Ut wisi enim ad minim veniam, quis nostrud exerci tation ullamcorper suscipit lobortis nisl ut aliquip ex ea commodo consequat. Duis autem vel eum iriure dolor in hendrerit in vulputate velit esse molestie consequat, vel illum dolore eu feugiat nulla facilisis at vero eros et accumsan.<br><br>Lorem ipsum dolor sit amet, consectetuer adipiscing elit, sed diam nonummy nibh euismod tincidunt ut laoreet dolore magna aliquam erat volutpat. Ut wisi enim ad minim veniam, quis nostrud exerci.</div>
  <div class="abs" style="left:178px;top:12px;width:172px;height:160px;background:var(--panel)"></div>
  <div class="abs" style="left:184px;top:28px"><span class="abs" style="left:0;top:0;width:22px;height:22px;border-radius:50%;background:var(--orange)"></span><div class="abs" style="left:32px;top:-2px;width:130px"><div class="mini-head">Lorem ipsum</div><div class="tiny">Ipsum dolor sit amet, consectetuer adipiscing elit, sed diam nonummy nibh euismod</div></div></div>
  <div class="abs" style="left:184px;top:78px"><span class="abs" style="left:0;top:0;width:22px;height:22px;border-radius:50%;background:var(--orange)"></span><div class="abs" style="left:32px;top:-2px;width:130px"><div class="mini-head">Lorem ipsum</div><div class="tiny">Ipsum dolor sit amet, consectetuer adipiscing elit, sed diam nonummy nibh euismod</div></div></div>
  <div class="abs" style="left:184px;top:128px"><span class="abs" style="left:0;top:0;width:22px;height:22px;border-radius:50%;background:var(--orange)"></span><div class="abs" style="left:32px;top:-2px;width:130px"><div class="mini-head">Lorem ipsum</div><div class="tiny">Ipsum dolor sit amet, consectetuer adipiscing elit, sed diam nonummy nibh euismod</div></div></div>
  <div class="foot">VANTOR<small>SOLAR</small></div><div class="rule"></div><div class="num">03</div>
</section>

<section class="slide slide-intelligence" style="left:50px;top:2133px">
  <div class="photo" role="img" aria-label="Photo of an installer in a hard hat lifting a solar panel" style="left:0;top:22px;width:185px;height:140px"></div>
  <div class="abs" style="left:20px;top:18px;width:60px;height:2px;background:var(--orange)"></div>
  <div class="abs" style="left:200px;top:16px;font-size:11px;color:var(--ink)">ACTIVE</div>
  <div class="s-title" style="left:200px;top:29px;font-size:12px"><span class="o">INTELLIGENCE</span></div>
  <div class="abs tiny" style="left:200px;top:44px;width:148px">Lorem ipsum dolor sit amet, consectetuer adipiscing elit, sed diam nonummy nibh euismod tincidunt ut laoreet dolore magna aliquam erat volutpat. Ut wisi enim ad minim veniam, quis nostrud exerci tation ullamcorper suscipit lobortis nisl ut aliquip ex ea commodo.<br><br>Lorem ipsum dolor sit amet, consectetuer adipiscing elit, sed diam nonummy nibh euismod tincidunt ut laoreet dolore magna aliquam erat volutpat, quis nostrud.</div>
  <div class="abs" style="left:200px;top:128px;width:148px;height:1px;background:var(--orange)"></div>
  <div class="abs tiny" style="left:212px;top:132px;width:136px">Lorem ipsum dolor sit amet, consectetuer adipiscing elit, sed diam nonummy nibh euismod</div>
  <div class="abs tiny" style="left:212px;top:152px;width:136px">Lorem ipsum dolor sit amet, consectetuer adipiscing elit, sed diam nonummy nibh euismod</div>
  <div class="foot">VANTOR<small>SOLAR</small></div><div class="rule"></div><div class="num">04</div>
</section>

<section class="slide slide-education" style="left:423px;top:2133px">
  <div class="s-title" style="left:12px;top:12px;font-size:12px;font-weight:500">OUR COMPANY <span class="o" style="font-weight:700">EDUCATION</span></div>
  <svg class="abs" style="left:60px;top:40px" width="250" height="100" viewBox="0 0 250 100">
    <g fill="none" stroke="var(--orange)" stroke-width="3">
      <rect x="4" y="6" width="62" height="88" rx="10"/>
      <rect x="92" y="6" width="62" height="88" rx="10"/>
      <rect x="180" y="6" width="62" height="88" rx="10"/>
      <path d="M66 40 H92 M154 40 H180"/>
    </g>
    <g fill="#fff" stroke="var(--ink)" stroke-width="1">
      <circle cx="79" cy="40" r="3"/><circle cx="167" cy="40" r="3"/>
    </g>
    <g font-family="Roboto,sans-serif" font-size="6" font-weight="700" fill="var(--orange)" text-anchor="middle">
      <text x="35" y="36">IDEA</text><text x="123" y="36">PROMOTION</text><text x="211" y="36">GROWTH</text>
    </g>
    <g fill="none" stroke="var(--ink)" stroke-width="1">
      <circle cx="35" cy="22" r="4"/><rect x="118" y="18" width="10" height="7"/><path d="M206 26 L216 18 M212 18 H216 V22"/>
    </g>
    <g font-family="Roboto,sans-serif" font-size="3.6" fill="#777" text-anchor="middle">
      <text x="35" y="46">Lorem ipsum dolor sit</text><text x="35" y="51">amet, consectetuer</text><text x="35" y="56">adipiscing elit, sed</text><text x="35" y="61">diam nonummy nibh</text>
      <text x="123" y="46">Lorem ipsum dolor sit</text><text x="123" y="51">amet, consectetuer</text><text x="123" y="56">adipiscing elit, sed</text><text x="123" y="61">diam nonummy nibh</text>
      <text x="211" y="46">Lorem ipsum dolor sit</text><text x="211" y="51">amet, consectetuer</text><text x="211" y="56">adipiscing elit, sed</text><text x="211" y="61">diam nonummy nibh</text>
    </g>
  </svg>
  <div class="abs tiny" style="left:40px;top:148px;width:282px;text-align:center">Lorem ipsum dolor sit amet, consectetuer adipiscing elit, sed diam nonummy nibh euismod tincidunt ut laoreet dolore magna aliquam erat volutpat. Ut wisi enim ad minim veniam, quis nostrud exerci tation ullamcorper suscipit lobortis nisl ut aliquip ex ea commodo.</div>
  <div class="foot">VANTOR<small>SOLAR</small></div><div class="rule"></div><div class="num">05</div>
</section>

<section class="slide slide-domain" style="left:797px;top:2133px">
  <div class="abs" style="left:0;top:0;width:26px;height:36px;background:var(--orange)"></div>
  <div class="photo" role="img" aria-label="Photo of installers carrying a panel across a rooftop array" style="left:18px;top:24px;width:160px;height:140px"></div>
  <div class="abs" style="left:188px;top:24px;font-size:9px;color:var(--ink);line-height:1.25">WHAT'S A DOMAIN?<br>IT'S THAT NAME UP</div>
  <div class="s-title" style="left:188px;top:48px;font-size:9.5px"><span class="o">IN THE ADDRESS BAR.</span></div>
  <div class="abs" style="left:188px;top:66px;font-size:6.6px;color:#666;line-height:2.1">
    <div><span class="dot-orange"></span>Fits your business or products</div>
    <div><span class="dot-orange"></span>Is easy to spell and remember</div>
    <div><span class="dot-orange"></span>Fits your business or products</div>
    <div><span class="dot-orange"></span>Is easy to spell and remember</div>
    <div><span class="dot-orange"></span>Fits your business or products</div>
    <div><span class="dot-orange"></span>Fits your business or products</div>
  </div>
  <div class="foot">VANTOR<small>SOLAR</small></div><div class="rule"></div><div class="num">06</div>
</section>

<section class="slide slide-overview" style="left:50px;top:2348px">
  <div class="abs" style="left:12px;top:8px;font-size:11px;font-weight:700;color:var(--ink)">COMPANY</div>
  <div class="s-title" style="left:12px;top:20px;font-size:18px"><span class="o">OVERVIEW</span></div>
  <div class="abs tiny" style="left:12px;top:42px;width:150px">Lorem ipsum dolor sit amet, consectetuer adipiscing elit, sed diam nonummy nibh euismod tincidunt ut laoreet dolore magna aliquam erat volutpat. Ut wisi enim ad minim veniam, quis nostrud exerci tation ullamcorper suscipit lobortis nisl ut aliquip ex ea commodo consequat.<br>Lorem ipsum dolor sit amet, consectetuer adipiscing elit, sed diam nonummy nibh.</div>
  <svg class="abs" style="left:185px;top:14px" width="165" height="86" viewBox="0 0 165 86">
    <g stroke="#e2e2e2" stroke-width=".5"><path d="M10 4H160M10 16H160M10 28H160M10 40H160M10 52H160M10 64H160"/></g>
    <g font-size="4" fill="#777" font-family="Roboto,sans-serif"><text x="0" y="6">60</text><text x="0" y="18">50</text><text x="0" y="30">40</text><text x="0" y="42">30</text><text x="0" y="54">20</text><text x="0" y="66">10</text><text x="30" y="80">JAN</text><text x="68" y="80">FEB</text><text x="104" y="80">MAR</text><text x="140" y="80">APR</text></g>
    <g fill="var(--ink)"><rect x="24" y="20" width="4" height="54"/><rect x="62" y="30" width="4" height="44"/><rect x="100" y="14" width="4" height="60"/><rect x="136" y="40" width="4" height="34"/></g>
    <g fill="var(--orange)"><rect x="30" y="10" width="4" height="64"/><rect x="68" y="44" width="4" height="30"/><rect x="106" y="24" width="4" height="50"/><rect x="142" y="8" width="4" height="66"/></g>
  </svg>
  <svg class="abs" style="left:10px;top:106px" width="170" height="72" viewBox="0 0 170 72">
    <g stroke="#e2e2e2" stroke-width=".5"><path d="M10 4H166M10 16H166M10 28H166M10 40H166M10 52H166M10 64H166"/></g>
    <path d="M12 60 L32 48 L52 58 L72 20 L92 44 L112 28 L132 40 L152 18 L166 30" fill="none" stroke="var(--orange)" stroke-width="1"/>
    <path d="M12 64 L32 52 L52 36 L72 42 L92 30 L112 46 L132 24 L152 34 L166 22" fill="none" stroke="var(--ink)" stroke-width="1"/>
  </svg>
  <div class="abs" style="left:190px;top:112px;width:160px">
    <div class="abs" style="left:0;top:0;width:75px"><div class="mini-head" style="font-size:5px"><span class="dot-orange"></span>Lorem ipsum</div><div class="tiny" style="font-size:3.6px">Lorem ipsum dolor sit amet, consectetuer adipiscing elit</div></div>
    <div class="abs" style="left:82px;top:0;width:75px"><div class="mini-head" style="font-size:5px;color:var(--ink)"><span class="dot-orange" style="background:var(--ink)"></span>Lorem ipsum</div><div class="tiny" style="font-size:3.6px">Lorem ipsum dolor sit amet, consectetuer adipiscing elit</div></div>
    <div class="abs" style="left:0;top:26px;width:75px"><div class="mini-head" style="font-size:5px;color:var(--ink)"><span class="dot-orange" style="background:var(--ink)"></span>Lorem ipsum</div><div class="tiny" style="font-size:3.6px">Lorem ipsum dolor sit amet, consectetuer adipiscing elit</div></div>
    <div class="abs" style="left:82px;top:26px;width:75px"><div class="mini-head" style="font-size:5px"><span class="dot-orange"></span>Lorem ipsum</div><div class="tiny" style="font-size:3.6px">Lorem ipsum dolor sit amet, consectetuer adipiscing elit</div></div>
  </div>
  <div class="foot">VANTOR<small>SOLAR</small></div><div class="rule"></div><div class="num">07</div>
</section>

<section class="slide slide-divider" style="left:423px;top:2348px;background:var(--orange)">
  <div class="abs" role="img" aria-label="Orange-tinted photo of a solar installation site" style="inset:0;background:radial-gradient(ellipse 40% 50% at 25% 60%, rgba(200,70,30,.7), rgba(200,70,30,0) 70%),radial-gradient(ellipse 35% 45% at 80% 35%, rgba(250,140,100,.6), rgba(250,140,100,0) 70%),linear-gradient(135deg,#e65a2c,#f47a4a 50%,#d9501f)"></div>
  <div class="abs" style="left:117px;top:44px;width:128px;height:110px;border:1.5px solid #fff"></div>
  <div class="abs" style="left:117px;top:54px;width:128px;text-align:center;color:#fff;font-family:'Roboto Condensed',sans-serif;font-weight:700;font-size:27px;line-height:1.08">ABOUT<br>OUR<br>PROJECT</div>
</section>

<section class="slide slide-portfolio" style="left:797px;top:2348px">
  <div class="photo plans" role="img" aria-label="Photo of engineering plans on a desk" style="left:20px;top:16px;width:130px;height:140px"></div>
  <div class="abs" style="left:150px;top:16px;width:2px;height:140px;background:var(--orange)"></div>
  <div class="abs" style="left:164px;top:20px;font-size:8px;color:var(--ink)">PORTFOLIO OF</div>
  <div class="s-title" style="left:164px;top:30px;font-size:17px"><span class="o">PROJECTS</span></div>
  <div class="abs tiny" style="left:164px;top:50px;width:186px">Lorem ipsum dolor sit amet, consectetuer adipiscing elit, sed diam nonummy nibh euismod tincidunt ut laoreet dolore magna aliquam erat volutpat. Ut wisi enim ad minim veniam, quis nostrud exerci tation ullamcorper suscipit lobortis nisl ut aliquip ex ea commodo consequat. Duis autem vel eum iriure dolor in hendrerit in vulputate velit esse.<br>Lorem ipsum dolor sit amet, consectetuer adipiscing elit, sed diam nonummy nibh euismod tincidunt ut laoreet dolore magna aliquam erat volutpat.</div>
  <div class="abs" style="left:174px;top:128px;width:176px;height:9px;background:#555"></div>
  <div class="abs tiny" style="left:174px;top:142px;width:176px">Lorem ipsum dolor sit amet, consectetuer adipiscing elit, sed diam nonummy nibh euismod</div>
  <div class="foot">VANTOR<small>SOLAR</small></div><div class="rule"></div><div class="num">09</div>
</section>

<section class="slide slide-usecases" style="left:50px;top:2563px">
  <div class="abs" role="img" aria-label="Illustration of three smartphones showing app screens" style="left:20px;top:10px;width:150px;height:155px;background:linear-gradient(135deg,#f2f2f2,#e3e3e3)"></div>
  <div class="s-title" style="left:186px;top:56px;font-size:22px;font-weight:400">USE <span class="o" style="font-weight:700">CASES</span></div>
  <div class="abs tiny" style="left:186px;top:84px;width:162px">Lorem ipsum dolor sit amet, consectetuer adipiscing elit, sed diam nonummy nibh euismod tincidunt ut laoreet dolore magna aliquam erat volutpat. Ut wisi enim ad minim veniam, quis nostrud exerci tation ullamcorper suscipit lobortis nisl ut aliquip.<br><br>Lorem ipsum dolor sit amet, consectetuer adipiscing elit, sed diam nonummy nibh euismod tincidunt ut laoreet dolore magna aliquam erat volutpat, quis nostrud exerci.</div>
  <div class="foot">VANTOR<small>SOLAR</small></div><div class="rule"></div><div class="num">10</div>
</section>

<section class="slide slide-project" style="left:423px;top:2563px">
  <div class="abs" style="left:0;right:0;top:22px;text-align:center;font-size:12px;color:var(--ink)">LOREM IPSUM <b style="color:var(--orange)">PROJECT</b></div>
  <div class="abs tiny" style="left:44px;top:38px;width:274px;text-align:center">Lorem ipsum dolor sit amet, consectetuer adipiscing elit, sed diam nonummy nibh euismod tincidunt ut laoreet dolore magna aliquam erat volutpat. Ut wisi enim ad minim veniam, quis nostrud exerci tation ullamcorper suscipit lobortis nisl ut aliquip ex ea.</div>
  <div class="photo" role="img" aria-label="Photo of a rooftop install" style="left:24px;top:74px;width:72px;height:48px"></div>
  <div class="photo panel-carry" role="img" aria-label="Photo of installers at work" style="left:104px;top:74px;width:72px;height:48px"></div>
  <div class="photo" role="img" aria-label="Photo of a crew on a roof" style="left:184px;top:74px;width:72px;height:48px"></div>
  <div class="photo panel-carry" role="img" aria-label="Photo of a finished solar array" style="left:264px;top:74px;width:72px;height:48px"></div>
  <div class="abs" style="left:24px;top:126px;width:312px;display:flex;gap:8px">
    <div style="width:72px"><div class="mini-head" style="font-size:5px">Lorem ipsum</div><div class="tiny" style="font-size:3.6px">Lorem ipsum dolor sit amet, consectetuer adipiscing elit, sed diam</div></div>
    <div style="width:72px"><div class="mini-head" style="font-size:5px">Lorem ipsum</div><div class="tiny" style="font-size:3.6px">Lorem ipsum dolor sit amet, consectetuer adipiscing elit, sed diam</div></div>
    <div style="width:72px"><div class="mini-head" style="font-size:5px">Lorem ipsum</div><div class="tiny" style="font-size:3.6px">Lorem ipsum dolor sit amet, consectetuer adipiscing elit, sed diam</div></div>
    <div style="width:72px"><div class="mini-head" style="font-size:5px">Lorem ipsum</div><div class="tiny" style="font-size:3.6px">Lorem ipsum dolor sit amet, consectetuer adipiscing elit, sed diam</div></div>
  </div>
  <div class="foot">VANTOR<small>SOLAR</small></div><div class="rule"></div><div class="num">11</div>
</section>

<section class="slide slide-steps" style="left:797px;top:2563px">
  <div class="abs" style="left:20px;top:12px;font-size:11px;font-weight:500;color:var(--ink)">STARTING</div>
  <div class="s-title" style="left:20px;top:24px;font-size:12px"><span class="o">LOREM IPSUM</span></div>
  <div class="abs" role="img" aria-label="Stepped infographic rising to an arrow" style="left:162px;top:12px;width:98px;height:168px;background:linear-gradient(180deg,var(--orange) 0%,#e0582c 45%,#4a4a4a 75%,#3a3a3a 100%);clip-path:polygon(50% 0,100% 22%,100% 100%,0 100%,0 22%)"></div>
  <div class="abs" style="left:80px;top:78px;width:80px;height:14px;background:var(--orange);color:#fff;font-size:8px;font-weight:700;line-height:14px;padding-left:4px">50%</div>
  <div class="abs" style="left:66px;top:100px;width:94px;height:14px;background:var(--ink);color:#fff;font-size:8px;font-weight:700;line-height:14px;padding-left:4px">40%</div>
  <div class="abs" style="left:52px;top:122px;width:108px;height:14px;background:var(--orange);color:#fff;font-size:8px;font-weight:700;line-height:14px;padding-left:4px">30%</div>
  <div class="abs" style="left:38px;top:144px;width:122px;height:14px;background:var(--ink);color:#fff;font-size:8px;font-weight:700;line-height:14px;padding-left:4px">20%</div>
  <div class="abs" style="left:270px;top:24px;width:84px">
    <div class="mini-head" style="font-size:5px"><span class="dot-orange"></span>Lorem ipsum</div><div class="tiny" style="font-size:3.6px;margin-bottom:10px">Lorem ipsum dolor sit amet, consectetuer adipiscing elit</div>
    <div class="mini-head" style="font-size:5px;color:var(--ink)"><span class="dot-orange" style="background:var(--ink)"></span>Lorem ipsum</div><div class="tiny" style="font-size:3.6px;margin-bottom:10px">Lorem ipsum dolor sit amet, consectetuer adipiscing elit</div>
    <div class="mini-head" style="font-size:5px"><span class="dot-orange"></span>Lorem ipsum</div><div class="tiny" style="font-size:3.6px;margin-bottom:10px">Lorem ipsum dolor sit amet, consectetuer adipiscing elit</div>
    <div class="mini-head" style="font-size:5px;color:var(--ink)"><span class="dot-orange" style="background:var(--ink)"></span>Lorem ipsum</div><div class="tiny" style="font-size:3.6px">Lorem ipsum dolor sit amet, consectetuer adipiscing elit</div>
  </div>
  <div class="foot">VANTOR<small>SOLAR</small></div><div class="rule"></div><div class="num">12</div>
</section>

<section class="slide slide-roadmap" style="left:50px;top:2778px">
  <svg class="abs" style="left:0;top:0" width="362" height="203" viewBox="0 0 362 203">
    <path d="M340 150 Q352 110 320 96 Q290 86 260 100 Q240 112 220 90 Q200 66 175 74 Q150 82 140 58 Q130 36 116 42" fill="none" stroke="var(--ink)" stroke-width="1.2"/>
    <path d="M205 118 Q206 146 240 148 L340 150" fill="none" stroke="var(--orange)" stroke-width="1.4"/>
    <path d="M340 150 V172" stroke="var(--ink)" stroke-dasharray="2 2"/>
    <g font-family="Roboto,sans-serif" font-weight="700" text-anchor="middle">
      <circle cx="330" cy="118" r="18" fill="#fff" stroke="var(--ink)" stroke-width="3"/><text x="330" y="128" font-size="26" fill="var(--orange)">1</text>
      <circle cx="224" cy="108" r="11" fill="#fff" stroke="var(--ink)" stroke-width="2"/><text x="224" y="114" font-size="15" fill="var(--orange)">2</text>
      <circle cx="274" cy="78" r="9" fill="#fff" stroke="var(--ink)" stroke-width="2"/><text x="274" y="83" font-size="12" fill="var(--orange)">3</text>
      <circle cx="186" cy="72" r="7" fill="#fff" stroke="var(--ink)" stroke-width="1.5"/><text x="186" y="76" font-size="9" fill="var(--orange)">4</text>
      <circle cx="208" cy="48" r="6" fill="#fff" stroke="var(--ink)" stroke-width="1.5"/><text x="208" y="51" font-size="7" fill="var(--orange)">5</text>
      <circle cx="166" cy="30" r="5" fill="#fff" stroke="var(--ink)" stroke-width="1"/><text x="166" y="33" font-size="6" fill="var(--orange)">6</text>
    </g>
  </svg>
  <div class="abs" style="left:120px;top:22px;width:46px"><div class="mini-head" style="font-size:4.6px">Lorem ipsum</div><div class="tiny" style="font-size:3.4px">Lorem ipsum dolor sit amet, consectetuer</div></div>
  <div class="abs" style="left:222px;top:20px;width:46px"><div class="mini-head" style="font-size:4.6px">Lorem ipsum</div><div class="tiny" style="font-size:3.4px">Lorem ipsum dolor sit amet, consectetuer</div></div>
  <div class="abs" style="left:290px;top:22px;width:46px"><div class="mini-head" style="font-size:4.6px">Lorem ipsum</div><div class="tiny" style="font-size:3.4px">Lorem ipsum dolor sit amet, consectetuer</div></div>
  <div class="abs" style="left:136px;top:84px;width:46px"><div class="mini-head" style="font-size:4.6px">Lorem ipsum</div><div class="tiny" style="font-size:3.4px">Lorem ipsum dolor sit amet, consectetuer</div></div>
  <div class="abs" style="left:256px;top:124px;width:46px"><div class="mini-head" style="font-size:4.6px">Lorem ipsum</div><div class="tiny" style="font-size:3.4px">Lorem ipsum dolor sit amet, consectetuer</div></div>
  <div class="abs" style="left:18px;top:80px;font-size:10px;letter-spacing:.08em;color:var(--ink)">TIMELINE OF</div>
  <div class="s-title" style="left:18px;top:92px;font-size:16px"><span class="o">ROADMAP</span></div>
  <div class="abs" style="left:18px;top:110px;font-size:7px;font-weight:700;color:var(--ink)">FOR 2 YEARS</div>
  <div class="abs" style="left:18px;top:126px;display:flex;align-items:center;gap:4px;font-size:9px;font-weight:700;color:var(--ink)"><span style="width:16px;height:16px;border-radius:50%;background:var(--orange);color:#fff;text-align:center;line-height:16px;font-size:8px">A</span>2019</div>
  <div class="abs" style="left:100px;top:126px;display:flex;align-items:center;gap:4px;font-size:9px;font-weight:700;color:var(--ink)"><span style="width:16px;height:16px;border-radius:50%;background:var(--orange);color:#fff;text-align:center;line-height:16px;font-size:8px">B</span>2020</div>
  <div class="abs tiny" style="left:38px;top:144px;width:54px;font-size:3.4px">Lorem ipsum dolor sit amet, consectetuer adipiscing</div>
  <div class="abs tiny" style="left:120px;top:144px;width:54px;font-size:3.4px">Lorem ipsum dolor sit amet, consectetuer adipiscing</div>
  <div class="foot">VANTOR<small>SOLAR</small></div><div class="rule"></div><div class="num">13</div>
</section>

<section class="slide slide-team" style="left:423px;top:2778px">
  <div class="abs" style="left:0;right:0;top:22px;text-align:center;font-size:10px;font-weight:500;color:var(--ink)">TEAM MEMBERS <b style="color:var(--orange)">AND ADVISORS</b></div>
  <div class="abs tiny" style="left:20px;top:36px;width:322px;text-align:center">Lorem ipsum dolor sit amet, consectetuer adipiscing elit, sed diam nonummy nibh euismod tincidunt ut laoreet dolore magna aliquam erat volutpat. Ut wisi enim ad minim veniam, quis nostrud exerci tation ullamcorper suscipit lobortis nisl ut aliquip ex ea commodo consequat.</div>
  <div class="abs" style="left:0;right:0;top:78px;height:88px;background:var(--orange)"></div>
  <div class="abs" style="left:20px;top:66px;width:322px;display:flex;justify-content:space-between">
    <div style="width:70px;text-align:center"><div role="img" aria-label="Portrait of a team member" style="width:28px;height:28px;margin:0 auto;border-radius:50%;background:radial-gradient(circle at 50% 40%,#c9c3bc,#8f8b87);border:2px solid #fff"></div><div style="font-size:5.6px;font-weight:700;color:#fff;margin-top:4px">OWEN HARTLEY</div><div style="font-size:3.6px;line-height:1.4;color:#fff">Lorem ipsum dolor sit amet, consectetuer adipiscing elit, sed diam nonummy</div></div>
    <div style="width:70px;text-align:center"><div role="img" aria-label="Portrait of a team member" style="width:28px;height:28px;margin:0 auto;border-radius:50%;background:radial-gradient(circle at 50% 40%,#c9c3bc,#8f8b87);border:2px solid #fff"></div><div style="font-size:5.6px;font-weight:700;color:#fff;margin-top:4px">NINA CALLOWAY</div><div style="font-size:3.6px;line-height:1.4;color:#fff">Lorem ipsum dolor sit amet, consectetuer adipiscing elit, sed diam nonummy</div></div>
    <div style="width:70px;text-align:center"><div role="img" aria-label="Portrait of a team member" style="width:28px;height:28px;margin:0 auto;border-radius:50%;background:radial-gradient(circle at 50% 40%,#c9c3bc,#8f8b87);border:2px solid #fff"></div><div style="font-size:5.6px;font-weight:700;color:#fff;margin-top:4px">OWEN HARTLEY</div><div style="font-size:3.6px;line-height:1.4;color:#fff">Lorem ipsum dolor sit amet, consectetuer adipiscing elit, sed diam nonummy</div></div>
    <div style="width:70px;text-align:center"><div role="img" aria-label="Portrait of a team member" style="width:28px;height:28px;margin:0 auto;border-radius:50%;background:radial-gradient(circle at 50% 40%,#c9c3bc,#8f8b87);border:2px solid #fff"></div><div style="font-size:5.6px;font-weight:700;color:#fff;margin-top:4px">NINA CALLOWAY</div><div style="font-size:3.6px;line-height:1.4;color:#fff">Lorem ipsum dolor sit amet, consectetuer adipiscing elit, sed diam nonummy</div></div>
  </div>
  <div class="foot">VANTOR<small>SOLAR</small></div><div class="rule"></div><div class="num">14</div>
</section>

<section class="slide slide-contact" style="left:797px;top:2778px">
  <div class="photo" role="img" aria-label="Photo of an installer in a hard hat working on a solar panel" style="left:150px;top:0;width:212px;height:203px;-webkit-mask-image:linear-gradient(90deg,transparent 0,#000 35%);mask-image:linear-gradient(90deg,transparent 0,#000 35%)"></div>
  <div class="brand" style="left:14px;top:18px;font-size:30px"><span class="b1">VANTOR</span><span class="b2" style="font-size:13px;margin-top:4px">SOLAR</span></div>
  <div class="abs" style="left:12px;top:104px;font-size:11px;font-weight:500;color:var(--ink)">CONTACT <span style="color:var(--orange);font-weight:700">US</span></div>
  <div class="abs" style="left:12px;top:122px;font-size:6.4px;color:#555;line-height:1.6">
    <div><span class="dot-orange"></span>555-010-333</div>
    <div><span class="dot-orange"></span>info@vantorcontact.example</div>
    <div><span class="dot-orange"></span>Your address, your city, box 88900</div>
  </div>
  <div class="abs" style="left:12px;top:164px;font-size:7px;letter-spacing:.15em;color:var(--ink)">www.<span style="color:var(--orange)">vantorsolar</span>.example</div>
  <div class="abs" style="left:9px;top:176px"><span class="soc"></span><span class="soc"></span><span class="soc"></span><span class="soc"></span></div>
</section>

</body>
</html>
```